Fine Dining Restaurant needs Harbour Stakes Day Flyer

We need a flyer to promote Harbour Stakes day at our restaurant in Port Douglas, QLD.
Details:
6th November 2018
It's a ticketed event, including a fine-dining 4 course lunch, with 3 hour drinks package, to include sweeps & prizes.
Starts 11:30 - 14:30.
Ticket price: $160 with $5 from each ticket going to Tails & Whiskers
Cash bar also available.
Address: 47 Copperleaf Lane, Port Douglas
Contact: 0740553819 or bookings@lorindas.net.au
*Big screen TV's
*Sweeps
*Best Dressed prizes and more...
*Glass of sparkling wine on arrival
*Discount for tables of 8 or more...
Design: we'd like to see a really elegant design for the flyer, with the use of tropical florals, utilising whites and some burnt orange colours if suitable.
Size: To be printed on A4

```html
<!DOCTYPE html>
<html lang="en">
<head>
<meta charset="utf-8">
<title>Harbour Stakes Day Flyer</title>
<link rel="stylesheet" href="https://fonts.googleapis.com/css2?family=Great+Vibes&family=Cinzel:wght@400&family=Montserrat:wght@400;500;700&display=swap">
<style>
  :root {
    --backdrop: #d9d9d9;
    --paper: #ffffff;
    --cream: #fdf0d9;
    --ink: #1d1a1a;
    --rule: #4a4545;
    --badge: #231f20;
    --badge-text: #ffffff;
    --bloom-orange: #f2a233;
    --bloom-yellow: #f6d43a;
    --bloom-blue: #6f86b3;
    --bloom-pink: #e67a8f;
    --bloom-blush: #f3c3c8;
    --bloom-red: #d93d5b;
    --leaf: #6fa56a;
  }
  * { margin: 0; padding: 0; box-sizing: border-box; }
  html, body {
    width: 1170px; height: 1200px; overflow: hidden;
    background: var(--backdrop);
  }
  .flyer {
    position: absolute; left: 175px; top: 20px;
    width: 820px; height: 1160px;
    background: var(--paper);
    box-shadow: 0 6px 18px rgba(0,0,0,0.18);
    overflow: hidden;
  }
  .panel {
    position: absolute; left: 38px; top: 38px; right: 48px; bottom: 38px;
    background: var(--cream);
  }
  .floral { position: absolute; }
  .floral--left {
    left: 0; top: 0; width: 170px; height: 300px;
    background:
      radial-gradient(circle at 62% 30%, var(--bloom-orange) 0 24%, transparent 25%),
      radial-gradient(circle at 22% 54%, var(--bloom-yellow) 0 22%, transparent 23%),
      radial-gradient(circle at 68% 8%, var(--bloom-blue) 0 12%, transparent 13%),
      radial-gradient(circle at 22% 86%, var(--bloom-blue) 0 10%, transparent 11%);
  }
  .floral--right {
    right: 0; top: 0; width: 150px; height: 270px;
    background:
      radial-gradient(circle at 40% 20%, var(--bloom-pink) 0 26%, transparent 27%),
      radial-gradient(circle at 88% 24%, var(--bloom-blush) 0 20%, transparent 21%),
      radial-gradient(circle at 48% 72%, var(--bloom-red) 0 26%, transparent 27%),
      radial-gradient(circle at 82% 50%, var(--leaf) 0 9%, transparent 10%);
  }
  .rider {
    position: absolute; left: 362px; top: 84px;
    width: 100px; height: 44px;
    background: var(--ink);
    border-radius: 40% 50% 30% 30%;
  }
  .title {
    position: absolute; left: 0; width: 100%; top: 140px;
    text-align: center;
    font-family: "Great Vibes", cursive; font-weight: 400;
    font-size: 70px; line-height: 84px; color: var(--ink);
  }
  .title-day {
    position: absolute; left: 0; width: 100%; top: 232px;
    text-align: center;
    font-family: "Montserrat", sans-serif; font-weight: 400;
    font-size: 34px; letter-spacing: 20px; padding-left: 20px; color: var(--ink);
  }
  .date-band {
    position: absolute; left: 140px; width: 492px; top: 298px; height: 52px;
    border-top: 1px solid var(--rule); border-bottom: 1px solid var(--rule);
    display: flex; align-items: center; justify-content: center;
    font-family: "Montserrat", sans-serif; font-size: 22px; letter-spacing: 10px;
    color: var(--ink);
  }
  .date-band sup { font-size: 12px; letter-spacing: 4px; }
  .hours {
    position: absolute; left: 0; width: 100%; top: 378px;
    text-align: center;
    font-family: "Montserrat", sans-serif; font-size: 21px; letter-spacing: 3px;
    color: var(--ink);
  }
  .features { position: absolute; left: 0; top: 0; list-style: none; }
  .feature {
    position: absolute; left: 162px;
    font-family: "Cinzel", serif; font-size: 23px; line-height: 30px;
    color: var(--ink); white-space: nowrap;
  }
  .feature-bloom {
    position: absolute; left: -54px; top: -2px;
    width: 40px; height: 40px; border-radius: 50%;
  }
  .bloom--pink { background: radial-gradient(circle, var(--ink) 0 12%, var(--bloom-pink) 14%); }
  .bloom--orange { background: radial-gradient(circle, #7a3c8a 0 12%, var(--bloom-orange) 14%); }
  .bloom--yellow { background: radial-gradient(circle, var(--ink) 0 14%, var(--bloom-yellow) 16%); }
  .ticket-badge {
    position: absolute; left: 478px; top: 459px;
    width: 220px; height: 220px; border-radius: 50%;
    background: var(--badge); color: var(--badge-text);
    text-align: center; font-family: "Montserrat", sans-serif;
    transform: rotate(6deg);
  }
  .ticket-label { position: absolute; top: 38px; width: 100%; font-size: 15px; letter-spacing: 3px; }
  .ticket-price { position: absolute; top: 60px; width: 100%; font-size: 60px; font-weight: 700; line-height: 1; }
  .ticket-price sup { font-size: 26px; vertical-align: 24px; }
  .ticket-note { position: absolute; top: 132px; width: 100%; font-size: 15px; line-height: 19px; }
  .cash-bar {
    position: absolute; left: 0; width: 100%; top: 918px;
    text-align: center;
    font-family: "Montserrat", sans-serif; font-size: 21px; letter-spacing: 3px;
    color: var(--ink);
  }
  .venue-name {
    position: absolute; left: 102px; top: 1004px;
    font-family: "Montserrat", sans-serif; font-weight: 700;
    font-size: 38px; line-height: 1; color: var(--ink);
  }
  .venue-address {
    position: absolute; left: 104px; top: 1064px;
    font-family: "Montserrat", sans-serif; font-size: 16px; color: var(--ink);
  }
  .contact-phone {
    position: absolute; left: 460px; top: 1018px;
    font-family: "Montserrat", sans-serif; font-weight: 700;
    font-size: 28px; letter-spacing: 2px; color: var(--ink);
  }
  .contact-email {
    position: absolute; left: 461px; top: 1054px;
    font-family: "Montserrat", sans-serif; font-size: 16px; color: var(--ink);
  }
</style>
</head>
<body>
  <main class="flyer">
    <div class="panel"></div>

    <div class="floral floral--left" role="img" aria-label="Watercolour tropical flowers in orange, yellow and blue with foliage"></div>
    <div class="floral floral--right" role="img" aria-label="Watercolour pink and red hibiscus flowers with leaves"></div>

    <div class="rider" role="img" aria-label="Silhouette of a jockey on a galloping racehorse"></div>
    <h1 class="title">Harbour Stakes</h1>
    <div class="title-day">DAY</div>

    <div class="date-band">6<sup>th</sup>&nbsp;November&nbsp;2018</div>
    <div class="hours">Starts 11:30 - 14:30</div>

    <ul class="features">
      <li class="feature" style="top:474px">
        <span class="feature-bloom bloom--pink" role="img" aria-label="Pink flower"></span>Fine-dining 4 course<br>lunch, with 3 hour<br>drinks package
      </li>
      <li class="feature" style="top:592px"><span class="feature-bloom bloom--orange" role="img" aria-label="Orange flower"></span>Big screen TV's</li>
      <li class="feature" style="top:652px"><span class="feature-bloom bloom--yellow" role="img" aria-label="Yellow flower"></span>Sweeps</li>
      <li class="feature" style="top:712px"><span class="feature-bloom bloom--pink" role="img" aria-label="Pink flower"></span>Best Dressed prizes and more...</li>
      <li class="feature" style="top:772px"><span class="feature-bloom bloom--orange" role="img" aria-label="Orange flower"></span>Glass of sparkling wine on arrival</li>
      <li class="feature" style="top:832px"><span class="feature-bloom bloom--yellow" role="img" aria-label="Yellow flower"></span>Discount for tables of 8 or more...</li>
    </ul>

    <div class="ticket-badge">
      <div class="ticket-label">TICKETS</div>
      <div class="ticket-price"><sup>$</sup>160</div>
      <div class="ticket-note">$5 from each ticket<br>is going to<br>Tails &amp; Whiskers</div>
    </div>

    <p class="cash-bar">Cash bar also available.</p>

    <div class="venue-name">LORINDA'S</div>
    <div class="venue-address">47 Copperleaf Lane, Port Douglas</div>

    <div class="contact-phone">07 4055 3819</div>
    <div class="contact-email">bookings@lorindas.net.au</div>
  </main>
</body>
</html>
```